FinTech company looking to revamp and expand client-facing interface for our financial models

Halvern Ledgerworks currently has a very simple website that allows clients to interact with our financial models. We are looking to completely redesign the current site and add several extra pages to provide extra functionality. We want the design to have a modern, slick feel, that will work on both a desktop or a tablet. It should be straightforward for clients to move between different pages at any time, and clear from the layout how to interact with the more advanced features. We have included screenshots of existing pages in the attached design brief, as well as sketches of the functionality required by the new pages, but can't provide a direct link to the current site.
Target Market(s)
Professional investors that will be paying to access the interface
Industry/Entity Type
Finance
Number of Pages Required
4 page
Colors
Designer to choose colors to be used in the design.
Look and feel
Each slider illustrates characteristics of the customer's brand and the style your logo design should communicate.

```html
<!DOCTYPE html>
<html lang="en">
<head>
<meta charset="utf-8">
<title>KORVA – Models &amp; Sensitivities</title>
<link href="https://fonts.googleapis.com/css2?family=Poppins:wght@400;500;600;700&display=swap" rel="stylesheet">
<style>
:root{
  --page:#e8ebf3;
  --panel:#ffffff;
  --side:#4d7cfe;
  --side-top:#6a8ff9;
  --side-active:#648efd;
  --side-sub:#5a86fd;
  --ink:#2b3040;
  --title:#3c4257;
  --muted:#8b93a7;
  --line:#eceef4;
  --row-alt:#fafbfd;
  --accent:#4d7cfe;
  --pill:#e9f0ff;
  --alert:#ff4d5e;
}
*{box-sizing:border-box;margin:0;padding:0}
html,body{width:753px;height:1200px;overflow:hidden}
body{background:var(--page);font-family:'Poppins',sans-serif;color:var(--ink);position:relative}
.screen{position:absolute;left:16px;width:720px;height:450px;background:var(--panel);overflow:hidden}
.screen.models{top:47px}
.screen.sens{top:539.5px}
.sidebar{position:absolute;left:0;top:0;width:132.5px;height:100%;background:var(--side)}
.brand{height:43.5px;background:var(--side-top);border-bottom:1px solid rgba(255,255,255,.25);display:flex;align-items:center;padding-left:26px;color:#fff;font-weight:600;font-size:17px;letter-spacing:.3px}
.nav{position:absolute;left:0;width:100%}
.nav-item{height:36px;display:flex;align-items:center;padding-left:27px;color:#fff;font-size:8.5px;font-weight:500;gap:11px}
.nav-item svg{width:10px;height:10px;flex:none}
.nav-item.active{background:var(--side-active);border-left:2px solid rgba(255,255,255,.35);padding-left:25px;font-weight:600}
.subnav{background:var(--side-sub);padding:4px 0 6px 52px}
.subnav a{display:block;color:rgba(255,255,255,.85);font-size:6.8px;height:18.5px;line-height:18.5px;text-decoration:none}
.subnav a.current{color:#fff;font-weight:600}
.main{position:absolute;left:132.5px;top:0;right:0;height:100%}
.topbar{height:43.5px;border-bottom:1px solid var(--line);display:flex;align-items:center;padding:0 20px}
.topbar h1{font-size:12px;font-weight:600;color:var(--title);flex:1}
.bell{width:10px;height:11px;position:relative;margin-right:13px}
.bell i{position:absolute;right:0;top:0;width:3px;height:3px;border-radius:50%;background:var(--alert)}
.avatar{width:16px;height:16px;border-radius:50%;background:radial-gradient(circle at 50% 40%,#8a6a55,#2a211d 70%)}
.toolbar{height:44px;display:flex;align-items:center;padding:0 20px}
.tabs{display:flex;flex:1;gap:4px}
.tab{height:20px;padding:0 11px;border-radius:10px;font-size:7px;font-weight:500;line-height:20px;color:var(--ink)}
.tab.on{background:var(--pill);color:var(--accent);font-weight:600}
.btn{height:20px;border:1px solid var(--line);border-radius:10px;display:flex;align-items:center;gap:7px;padding:0 11px;font-size:7px;margin-left:7px}
.btn svg{width:8px;height:8px}
.btn.on{background:var(--pill);border-color:#dbe5ff;color:var(--accent)}
.thresholds{margin:0 20px;border-top:1px solid var(--line);padding:13px 0 0 17.5px;height:93px;border-bottom:none}
.th-grid{display:grid;grid-template-columns:repeat(5,104.5px);row-gap:9px}
.th-field label{display:block;font-size:7px;font-weight:500;color:var(--ink);margin-bottom:4px}
.th-field span{display:block;width:92.5px;height:17px;border:1px solid var(--line);border-radius:9px}
.table{border-top:1px solid var(--line)}
.row{display:grid;align-items:start;padding-left:20px;height:37px;border-bottom:1px solid var(--line);font-size:6px;padding-top:10px;line-height:10px}
.row.head{height:29px;padding-top:0;align-items:center;color:var(--muted);font-size:7px;font-weight:500}
.row.alt{background:var(--row-alt)}
.models .row{grid-template-columns:29.5px 50px 101px 64px 71px 54px 55px 56px 56px 1fr}
.sens .row{grid-template-columns:29.5px 61px 61px 107px 55px 55px 56px 56px 56px 1fr}
.sort::after{content:"⇕";font-size:5px;margin-left:3px}
.heart{width:8px;height:8px;margin-top:1px}
.head .heart{margin-top:0}
.strong{font-weight:600}
.note{position:absolute;left:22px;top:1012px;width:712px;font-size:12.4px;line-height:18px;font-weight:500;color:var(--title)}
.note p{margin-bottom:18px}
</style>
</head>
<body>

<svg width="0" height="0" style="position:absolute">
  <defs>
    <symbol id="i-heart" viewBox="0 0 24 24"><path d="M12 20.5 3.8 12.6A5 5 0 0 1 12 6.2a5 5 0 0 1 8.2 6.4Z" fill="none" stroke="currentColor" stroke-width="2" stroke-linejoin="round"/></symbol>
    <symbol id="i-heart-fill" viewBox="0 0 24 24"><path d="M12 20.5 3.8 12.6A5 5 0 0 1 12 6.2a5 5 0 0 1 8.2 6.4Z" fill="currentColor"/></symbol>
    <symbol id="i-home" viewBox="0 0 24 24"><path d="M3 11 12 3l9 8v10H3Zm6 10v-6h6v6" fill="none" stroke="currentColor" stroke-width="2" stroke-linejoin="round"/></symbol>
    <symbol id="i-gear" viewBox="0 0 24 24"><circle cx="12" cy="12" r="3" fill="none" stroke="currentColor" stroke-width="2"/><path d="M12 2.5l2 2.3 3-.6.9 2.9 2.9.9-.6 3 2.3 2-2.3 2 .6 3-2.9.9-.9 2.9-3-.6-2 2.3-2-2.3-3 .6-.9-2.9-2.9-.9.6-3L1.5 12l2.3-2-.6-3 2.9-.9.9-2.9 3 .6Z" fill="none" stroke="currentColor" stroke-width="1.8" stroke-linejoin="round"/></symbol>
    <symbol id="i-case" viewBox="0 0 24 24"><rect x="2.5" y="7" width="19" height="13" rx="1.5" fill="none" stroke="currentColor" stroke-width="2"/><path d="M8.5 7V4h7v3M8.5 7v13M15.5 7v13" fill="none" stroke="currentColor" stroke-width="2"/></symbol>
    <symbol id="i-bell" viewBox="0 0 24 24"><path d="M5 17h14l-2-3V9a5 5 0 0 0-10 0v5Zm5 3a2 2 0 0 0 4 0" fill="none" stroke="currentColor" stroke-width="2" stroke-linejoin="round"/></symbol>
    <symbol id="i-filter" viewBox="0 0 24 24"><path d="M3 6h18M6 12h12M10 18h4" stroke="currentColor" stroke-width="2.4" stroke-linecap="round"/></symbol>
    <symbol id="i-export" viewBox="0 0 24 24"><path d="M7 17H6a4 4 0 0 1 0-8 6 6 0 0 1 11.5-1A4.5 4.5 0 0 1 18 17h-1M12 11v9m-3-3 3 3 3-3" fill="none" stroke="currentColor" stroke-width="2" stroke-linecap="round" stroke-linejoin="round"/></symbol>
  </defs>
</svg>

<!-- Models screen -->
<section class="screen models">
  <aside class="sidebar">
    <div class="brand">KORVA</div>
    <nav class="nav" style="top:88px">
      <div class="nav-item active"><svg><use href="#i-home"/></svg>Models</div>
      <div class="nav-item"><svg><use href="#i-gear"/></svg>Sensitivities</div>
      <div class="nav-item"><svg><use href="#i-heart"/></svg>Favourites</div>
      <div class="nav-item"><svg><use href="#i-case"/></svg>Portfolio</div>
    </nav>
  </aside>
  <div class="main">
    <header class="topbar">
      <h1>Models</h1>
      <div class="bell"><svg width="10" height="11"><use href="#i-bell"/></svg><i></i></div>
      <div class="avatar" role="img" aria-label="User profile photo"></div>
    </header>
    <div class="toolbar">
      <div class="tabs"><span class="tab on">250D</span><span class="tab">83D</span><span class="tab">42D</span></div>
      <span class="btn"><svg><use href="#i-filter"/></svg>Filters</span>
      <span class="btn"><svg><use href="#i-export"/></svg>Export Data</span>
    </div>
    <div class="table">
      <div class="row head"><svg class="heart"><use href="#i-heart"/></svg><span class="sort">ID</span><span class="sort">Sector</span><span class="sort">Time</span><span class="sort">Quantity</span><span class="sort">Stat 1</span><span class="sort">Stat 2</span><span class="sort">Stat 3</span><span class="sort">Stat 4</span><span class="sort">Stat 5</span></div>
      <div class="row"><svg class="heart" style="color:var(--accent)"><use href="#i-heart-fill"/></svg><span>Model 1</span><span>Consumer Discretionary</span><span>2019-04-01<br>12:15 pm</span><span>30.2288</span><span>2.01574</span><span>23.305</span><span>-0.149368</span><span>22.3054</span><span class="strong">4.63714</span></div>
      <div class="row alt"><svg class="heart" style="color:var(--muted)"><use href="#i-heart"/></svg><span>Model 2</span><span>Materials</span><span>2019-04-01<br>12:15 pm</span><span>30.2288</span><span>2.01574</span><span>23.305</span><span>-0.149368</span><span>22.3054</span><span class="strong">4.63714</span></div>
      <div class="row"><svg class="heart" style="color:var(--accent)"><use href="#i-heart-fill"/></svg><span>Model 3</span><span>Industrials</span><span>2019-04-01<br>12:15 pm</span><span>30.2288</span><span>2.01574</span><span>23.305</span><span>-0.149368</span><span>22.3054</span><span class="strong">4.63714</span></div>
      <div class="row alt"><svg class="heart" style="color:var(--muted)"><use href="#i-heart"/></svg><span>Model 4</span><span>Information Technology</span><span>2019-04-01<br>12:15 pm</span><span>30.2288</span><span>2.01574</span><span>23.305</span><span>-0.149368</span><span>22.3054</span><span class="strong">4.63714</span></div>
    </div>
  </div>
</section>

<!-- Sensitivities screen -->
<section class="screen sens">
  <aside class="sidebar">
    <div class="brand">KORVA</div>
    <nav class="nav" style="top:88px">
      <div class="nav-item"><svg><use href="#i-home"/></svg>Models</div>
      <div class="nav-item active"><svg><use href="#i-gear"/></svg>Sensitivities</div>
      <div class="subnav">
        <a>Equities</a><a>ETFS</a><a class="current">Pairs</a><a>ETF Pairs</a><a>Factors</a>
      </div>
      <div class="nav-item"><svg><use href="#i-heart"/></svg>Favourites</div>
      <div class="nav-item"><svg><use href="#i-case"/></svg>Portfolio</div>
    </nav>
  </aside>
  <div class="main">
    <header class="topbar">
      <h1>Sensitivities</h1>
      <div class="bell"><svg width="10" height="11"><use href="#i-bell"/></svg><i></i></div>
      <div class="avatar" role="img" aria-label="User profile photo"></div>
    </header>
    <div class="toolbar">
      <div class="tabs"><span class="tab">250D</span><span class="tab on">83D</span><span class="tab">42D</span></div>
      <span class="btn on"><svg><use href="#i-filter"/></svg>Filters</span>
      <span class="btn"><svg><use href="#i-export"/></svg>Export Data</span>
    </div>
    <div class="thresholds">
      <div class="th-grid">
        <div class="th-field"><label>Stat 1 Threshold</label><span></span></div>
        <div class="th-field"><label>Stat 2 Threshold</label><span></span></div>
        <div class="th-field"><label>Stat 3 Threshold</label><span></span></div>
        <div class="th-field"><label>Stat 4 Threshold</label><span></span></div>
        <div class="th-field"><label>Stat 5 Threshold</label><span></span></div>
        <div class="th-field"><label>Stat 6 Threshold</label><span></span></div>
        <div class="th-field"><label>Stat 7 Threshold</label><span></span></div>
        <div class="th-field"><label>Stat 8 Threshold</label><span></span></div>
        <div class="th-field"><label>Stat 9 Threshold</label><span></span></div>
        <div class="th-field"><label>Stat 10 Threshold</label><span></span></div>
      </div>
    </div>
    <div class="table">
      <div class="row head"><svg class="heart"><use href="#i-heart"/></svg><span class="sort">Factor</span><span class="sort">ID</span><span class="sort">Sector</span><span class="sort">Stat 1</span><span class="sort">Stat 2</span><span class="sort">Stat 3</span><span class="sort">Stat 4</span><span class="sort">Stat 5</span><span class="sort">Stat 6</span></div>
      <div class="row"><svg class="heart" style="color:var(--accent)"><use href="#i-heart-fill"/></svg><span>Factor 1</span><span>Model 1</span><span>Consumer Discretionary</span><span>30.2288</span><span>2.01574</span><span>23.305</span><span>-0.149368</span><span>22.3054</span><span>4.63714</span></div>
      <div class="row alt"><svg class="heart" style="color:var(--muted)"><use href="#i-heart"/></svg><span>Factor 2</span><span>Model 2</span><span>Materials</span><span>30.2288</span><span>2.01574</span><span>23.305</span><span>-0.149368</span><span>22.3054</span><span>4.63714</span></div>
      <div class="row"><svg class="heart" style="color:var(--accent)"><use href="#i-heart-fill"/></svg><span>Factor 3</span><span>Model 3</span><span>Industrials</span><span>30.2288</span><span>2.01574</span><span>23.305</span><span>-0.149368</span><span>22.3054</span><span class="strong">4.63714</span></div>
      <div class="row alt"><svg class="heart" style="color:var(--muted)"><use href="#i-heart"/></svg><span>Factor 4</span><span>Model 4</span><span>Information Technology</span><span>30.2288</span><span>2.01574</span><span>23.305</span><span>-0.149368</span><span>22.3054</span><span>4.63714</span></div>
    </div>
  </div>
</section>

<div class="note">
  <p>Hello Marisol, the project deadline is fast approaching and being that I entered the contest late I've not done so much but I'm really interested in this project.</p>
  <p>The above screens are for the Models and Sensitivities pages, please let me know if you're satisfied with the direction I'm taking with the designs, I'm also welcome to feedback on what can be improved to better suit your needs even as I continue and try to finish up everything including the new features before the deadline.</p>
  <p>Thank you.</p>
</div>

</body>
</html>
```